Business card design for new brand

We have recently rebranded and need a new business card template.

We are an insurance underwriting agency. All of our products are sold via other partner companies, so these are just to pass on our details to other organisations.

We would like to see designs that use the colour green (current stationary generally uses lime green (rgb 142,190,63) and forest green (0,154,79) to comply with our logo's colours. We are happy with other shades of green.

Business cards need to include our logo, as well as space for:
1. Full name
2. Qualifications (optional)
3. Title
4. Office number
5. Mobile number
6. Email address

Our logo is enclosed here.

```html
<!DOCTYPE html>
<html lang="en">
<head>
<meta charset="UTF-8">
<title>Coverline Australia – Business Card</title>
<link href="https://fonts.googleapis.com/css2?family=Open+Sans:wght@400;600;700&display=swap" rel="stylesheet">
<style>
  :root {
    --canvas: #262626;
    --card: #141414;
    --lime: #c6dc2a;
    --lime-soft: #8ebe3f;
    --forest: #009a4f;
    --forest-deep: #0b7a3a;
    --ink: #ffffff;
    --ink-muted: #e6e6e6;
    --ghost: #3a3a3a;
  }
  * { margin: 0; padding: 0; box-sizing: border-box; }
  html, body { width: 1200px; height: 900px; overflow: hidden; }
  body {
    background: var(--canvas);
    font-family: "Open Sans", Arial, sans-serif;
    display: flex;
    flex-direction: column;
    align-items: center;
    justify-content: center;
    gap: 60px;
  }
  .card {
    position: relative;
    width: 630px;
    height: 360px;
    background: var(--card);
    overflow: hidden;
    box-shadow: 0 18px 40px rgba(0,0,0,.55);
  }
  .card__edge {
    position: absolute;
    left: 0; right: 0; bottom: 0;
    height: 5px;
    background: linear-gradient(90deg, var(--lime) 0%, var(--lime-soft) 40%, var(--forest) 80%, var(--forest-deep) 100%);
  }

  /* Front */
  .card--front { display: flex; align-items: center; }
  .brand {
    width: 320px;
    padding-left: 48px;
    display: flex;
    align-items: flex-start;
    gap: 12px;
  }
  .brand__square {
    width: 30px; height: 30px;
    background: var(--forest);
    margin-top: 10px;
    flex: none;
  }
  .brand__name {
    color: var(--ink);
    font-weight: 600;
    font-size: 46px;
    line-height: 1;
    letter-spacing: -0.5px;
  }
  .brand__sub {
    color: var(--ink);
    font-weight: 400;
    font-size: 19px;
    margin-top: 6px;
    letter-spacing: 0.3px;
  }
  .divider {
    width: 1px;
    height: 150px;
    background: var(--forest);
    margin: 0 26px 0 6px;
  }
  .contact__name {
    color: var(--forest);
    font-weight: 700;
    font-size: 22px;
    letter-spacing: 0.3px;
    text-transform: uppercase;
  }
  .contact__title {
    color: var(--ink);
    font-size: 15px;
    margin-bottom: 10px;
  }
  .contact__list { list-style: none; }
  .contact__item {
    display: flex;
    align-items: center;
    gap: 9px;
    color: var(--ink);
    font-size: 14px;
    line-height: 23px;
  }
  .contact__item svg { width: 13px; height: 13px; flex: none; }

  /* Back */
  .card--back {
    display: flex;
    align-items: center;
    justify-content: center;
  }
  .back-brand { display: flex; align-items: flex-start; gap: 16px; }
  .back-brand__square {
    width: 44px; height: 44px;
    background: #0c0c0c;
    margin-top: 14px;
  }
  .back-brand__name {
    color: var(--ghost);
    font-weight: 600;
    font-size: 70px;
    line-height: 1;
  }
  .back-brand__sub {
    color: var(--ghost);
    font-size: 28px;
    margin-top: 6px;
    padding-left: 10px;
  }
</style>
</head>
<body>

  <section class="card card--front" aria-label="Business card front">
    <div class="brand">
      <span class="brand__square" aria-hidden="true"></span>
      <div>
        <div class="brand__name">Coverline</div>
        <div class="brand__sub">Australia Pty Ltd</div>
      </div>
    </div>
    <span class="divider" aria-hidden="true"></span>
    <div class="contact">
      <div class="contact__name">Daniel Harwood</div>
      <div class="contact__title">President</div>
      <ul class="contact__list">
        <li class="contact__item">
          <svg viewBox="0 0 16 16" aria-hidden="true"><path fill="var(--lime-soft)" d="M3.6 1.2 6 3.6 4.6 5.6c.9 2 2.6 3.8 4.8 4.8l2-1.4 2.4 2.4-1.6 2.4C6.8 13.6 2.4 9.2 1.2 2.8z"/></svg>
          555-014-2870
        </li>
        <li class="contact__item">
          <svg viewBox="0 0 16 16" aria-hidden="true"><rect x="4" y="1" width="8" height="14" rx="1.5" fill="none" stroke="var(--lime-soft)" stroke-width="1.6"/><circle cx="8" cy="12.3" r="0.9" fill="var(--lime-soft)"/></svg>
          555-014-2870
        </li>
        <li class="contact__item">
          <svg viewBox="0 0 16 16" aria-hidden="true"><rect x="1" y="3" width="14" height="10" fill="var(--lime-soft)"/><path d="M1 3l7 5.5L15 3" fill="none" stroke="var(--card)" stroke-width="1.3"/></svg>
          hello@coverlinemail.com
        </li>
        <li class="contact__item">
          <svg viewBox="0 0 16 16" aria-hidden="true"><circle cx="8" cy="8" r="6.5" fill="none" stroke="var(--lime-soft)" stroke-width="1.5"/><path d="M1.5 8h13M8 1.5c2.2 2 2.2 11 0 13M8 1.5c-2.2 2-2.2 11 0 13" fill="none" stroke="var(--lime-soft)" stroke-width="1.2"/></svg>
          www.coverlinesite.com
        </li>
      </ul>
    </div>
    <span class="card__edge" aria-hidden="true"></span>
  </section>

  <section class="card card--back" aria-label="Business card back">
    <div class="back-brand">
      <span class="back-brand__square" aria-hidden="true"></span>
      <div>
        <div class="back-brand__name">Coverline</div>
        <div class="back-brand__sub">Australia Pty Ltd</div>
      </div>
    </div>
    <span class="card__edge" aria-hidden="true"></span>
  </section>

</body>
</html>
```